Wren Hollow Apartments
stationary
Wren Hollow Apartments - Real Estate
Creative Brief
Traditional
Tobias Lindqvist
2408 Wren Hollow Houston TX 77091
tjlindqvist@quellmail.example

```html
<!DOCTYPE html>
<html lang="en">
<head>
<meta charset="utf-8">
<title>Wren Hollow Apartments — Business Card</title>
<link rel="stylesheet" href="https://fonts.googleapis.com/css2?family=Cinzel:wght@400;500&family=Cormorant+Garamond:wght@500&display=swap">
<style>
  :root {
    --green: #31893b;
    --green-dark: #23702d;
    --white: #ffffff;
    --ink: #161616;
    --backdrop: #e8e9e8;
  }
  * { box-sizing: border-box; margin: 0; padding: 0; }
  html, body {
    width: 1200px; height: 1009px; overflow: hidden;
    background: var(--backdrop);
  }
  .sheet {
    position: relative; width: 1200px; height: 1009px;
  }
  .card {
    position: absolute; left: 190px;
    width: 820px; height: 469px;
    border-radius: 26px; overflow: hidden;
    background: var(--green);
    box-shadow: 0 6px 18px rgba(0,0,0,0.12);
  }
  .card--back { top: 24px; }
  .card--front { top: 516px; }

  /* Back side */
  .back-mark {
    position: absolute; inset: 0;
    display: flex; flex-direction: column; align-items: center; justify-content: center;
    gap: 14px; color: var(--white);
    font-family: "Cinzel", serif; font-weight: 400;
  }
  .back-mark__dot {
    width: 62px; height: 62px; border-radius: 50%; background: var(--white);
  }
  .back-mark__name { font-size: 50px; letter-spacing: 1px; line-height: 1; }
  .back-mark__sub { font-size: 22px; letter-spacing: 9px; line-height: 1; }

  /* Front side */
  .front-shape { position: absolute; inset: 0; }
  .front-mark {
    position: absolute; left: 46px; top: 70px;
    display: flex; flex-direction: column; align-items: center; gap: 10px;
    color: var(--green);
    font-family: "Cinzel", serif; font-weight: 400;
  }
  .front-mark__dot { width: 46px; height: 46px; border-radius: 50%; background: var(--green); }
  .front-mark__name { font-size: 38px; line-height: 1; }
  .front-mark__sub { font-size: 16px; letter-spacing: 7px; line-height: 1; }

  .holder {
    position: absolute; right: 48px; top: 150px;
    color: var(--white);
    font-family: "Cinzel", serif; font-weight: 400;
    font-size: 25px; letter-spacing: 1px;
  }
  .contact {
    position: absolute; right: 48px; top: 268px;
    list-style: none; text-align: right;
    color: var(--white);
    font-family: "Cormorant Garamond", serif; font-weight: 500;
    font-size: 23px; line-height: 30px;
  }
  .contact li { display: flex; justify-content: flex-end; align-items: center; gap: 12px; }
  .contact__icon { width: 18px; height: 18px; flex: none; }
  .contact__spacer { width: 18px; flex: none; }
</style>
</head>
<body>
<main class="sheet">

  <section class="card card--back" aria-label="Card back">
    <div class="back-mark">
      <span class="back-mark__dot"></span>
      <span class="back-mark__name">Wren Hollow</span>
      <span class="back-mark__sub">APARTMENTS</span>
    </div>
  </section>

  <section class="card card--front" aria-label="Card front">
    <svg class="front-shape" viewBox="0 0 820 469" width="820" height="469" aria-hidden="true">
      <path d="M0 0 H492 C452 200 320 340 0 400 Z" fill="var(--ink)"/>
      <path d="M0 0 H470 C420 180 300 310 0 368 Z" fill="var(--white)"/>
    </svg>

    <div class="front-mark">
      <span class="front-mark__dot"></span>
      <span class="front-mark__name">Wren Hollow</span>
      <span class="front-mark__sub">APARTMENTS</span>
    </div>

    <h1 class="holder">TOBIAS LINDQVIST</h1>

    <ul class="contact">
      <li>2408 Wren Hollow<span class="contact__spacer"></span></li>
      <li>Houston TX 77091<span class="contact__spacer"></span></li>
      <li>713-555-0142
        <svg class="contact__icon" viewBox="0 0 24 24" aria-hidden="true"><path fill="var(--white)" d="M6.6 10.8a15.1 15.1 0 0 0 6.6 6.6l2.2-2.2a1 1 0 0 1 1-.25 11.4 11.4 0 0 0 3.6.57 1 1 0 0 1 1 1V20a1 1 0 0 1-1 1A17 17 0 0 1 3 4a1 1 0 0 1 1-1h3.5a1 1 0 0 1 1 1c0 1.25.2 2.45.57 3.57a1 1 0 0 1-.25 1z"/></svg>
      </li>
      <li>tjlindqvist@quellmail.example
        <svg class="contact__icon" viewBox="0 0 24 24" aria-hidden="true"><rect x="2" y="5" width="20" height="14" rx="1.5" fill="none" stroke="var(--white)" stroke-width="2"/><path d="M3 6l9 7 9-7" fill="none" stroke="var(--white)" stroke-width="2"/></svg>
      </li>
    </ul>
  </section>

</main>
</body>
</html>
```